Geschäftspapiere
Zielgruppe
Die TIVA Salbe gibt ein zuverlässige Gefühl, durch ein innovatives Naturprodukt erstaunlich schnelle, wirkungsvolle Hilfe bei Schmerzen des Bewegungsapparates und bei Hautschäden zu erhalten und dabei gleichzeitig die Haut zu pflegen.
Wir wollen jetzt stärker auf die Zielgruppe TCM Praxis, Chiropraktiker, Physiotherapie gehen und wollen nun eine Preisliste dafür erstellen.
Aufgabenstellung
Zielgruppe ist B2B, TCM Praxis, Chiropraktiker, Physiotherapie.
Die Preisliste sollte auf den Briefpapier erstellt werden. Bitte an Farben, Logos etc. von der Webseite nehmen.

```html
<!DOCTYPE html>
<html lang="de">
<head>
<meta charset="utf-8">
<title>TIVA Salbe – Preisliste</title>
<link href="https://fonts.googleapis.com/css2?family=Source+Sans+3:wght@400;600;700&display=swap" rel="stylesheet">
<style>
:root{
  --bg:#e4e8e4;
  --paper:#f3f3f3;
  --ink:#2b2b2b;
  --muted:#5c5c5c;
  --orange:#e9a31c;
  --green:#77a537;
  --teal:#35a7b1;
  --gold:#d9a827;
  --white:#ffffff;
}
*{margin:0;padding:0;box-sizing:border-box}
html,body{width:1200px;height:1012px;overflow:hidden;background:var(--bg);font-family:"Source Sans 3",sans-serif;color:var(--ink)}
.sheet{position:absolute;left:263px;top:23px;width:673px;height:965px;background:var(--paper);overflow:hidden}
.edge-rule{position:absolute;right:0;top:0;width:3px;height:100%;background:var(--orange)}
.brand-cap{position:absolute;left:430px;top:-80px;width:226px;height:255px;border-radius:0 0 113px 113px;background:var(--paper);box-shadow:0 3px 4px rgba(0,0,0,.18)}
.brand-dot{position:absolute;left:462px;top:62px;width:22px;height:22px;border-radius:50%;background:var(--gold)}
.brand-name{position:absolute;left:494px;top:54px;font-weight:700;font-size:34px;line-height:1;color:var(--ink)}
.brand-claim{position:absolute;left:494px;top:98px;font-size:12px;font-weight:600;letter-spacing:1.5px;color:var(--orange)}
.sender{position:absolute;left:78px;top:157px;font-size:7px;color:var(--muted)}
.sender b{font-weight:600}
.title{position:absolute;left:78px;top:273px;font-size:14px;font-weight:700;color:var(--orange);letter-spacing:.3px}
.title-rule{position:absolute;left:0;top:289px;width:76px;height:2px;background:var(--orange)}
.tick{position:absolute;left:0;top:339px;width:10px;height:2px;background:var(--orange)}
.intro{position:absolute;left:78px;top:298px;width:548px;font-size:11.4px;line-height:18px;color:var(--muted)}
.card{position:absolute;top:423px;width:144px;height:362px;border-radius:9px 9px 72px 72px/9px 9px 22px 22px;box-shadow:0 4px 2px rgba(0,0,0,.22);color:var(--white);text-align:center}
.card--starter{left:76px;background:var(--green)}
.card--premium{left:268px;background:var(--teal)}
.card--special{left:460px;background:var(--orange)}
.card__seal{position:absolute;left:27px;top:-31px;width:90px;height:90px;border-radius:50%;background:var(--white);border:5px solid var(--gold);box-shadow:0 0 0 3px var(--white)}
.card__label{position:absolute;left:7px;top:75px;width:130px;height:22px;background:var(--white);font-weight:700;font-size:19px;line-height:22px;letter-spacing:.5px}
.card--starter .card__label{color:var(--green)}
.card--premium .card__label{color:var(--teal)}
.card--special .card__label{color:var(--orange)}
.card__qty{position:absolute;left:0;top:113px;width:100%;font-size:18px;font-weight:600}
.card__price{position:absolute;left:0;top:159px;width:100%;font-size:15px;font-weight:600}
.card__rule{position:absolute;left:13px;width:118px;height:1.5px;background:rgba(255,255,255,.85)}
.card__text{position:absolute;left:6px;top:196px;width:132px;font-size:8.5px;font-weight:600;line-height:17px;white-space:nowrap}
.footer{position:absolute;left:0;top:864px;width:655px;height:101px;background:var(--orange);color:var(--white);font-size:7.5px;line-height:12.7px}
.footer__col{position:absolute;top:11px}
.footer__col b{font-weight:700}
.footer__sep{position:absolute;top:13px;width:1.5px;height:46px;background:var(--white)}
.footer__rule{position:absolute;left:4px;top:69px;width:651px;height:1.5px;background:var(--white)}
.footer__badges{position:absolute;left:0;top:75px;width:100%;height:18px}
.badge{position:absolute;top:0;width:18px;height:18px;border-radius:50%;background:#f3e3bc;border:1.5px solid #fff}
.badge--wide{width:34px;height:8px;top:5px;border-radius:1px}
.label-row span{display:inline-block;width:36px;font-weight:700}
</style>
</head>
<body>
<main class="sheet">
  <div class="edge-rule"></div>

  <header>
    <div class="brand-cap"></div>
    <div class="brand-dot"></div>
    <div class="brand-name">TIVA Salbe</div>
    <div class="brand-claim">LUMEN TIVA</div>
    <p class="sender"><b>Lindauer Medizin Vertrieb GmbH</b> · Birkenweg 14 · 80331 München</p>
  </header>

  <section>
    <h1 class="title">PREISLISTE:</h1>
    <div class="title-rule"></div>
    <div class="tick"></div>
    <p class="intro">Lorem ipsum dolor sit amet, consectetuer adipiscing elit, sed diam nonummy nibh euismod tincidunt ut laoreet<br>dolore magna aliquam erat volutpat. Ut wisi enim ad minim veniam, quis nostrud exerci tation ullamcorper<br>suscipit lobortis</p>

    <article class="card card--starter">
      <div class="card__seal"></div>
      <h2 class="card__label">STARTER</h2>
      <div class="card__qty">5 Tuben</div>
      <div class="card__rule" style="top:147px"></div>
      <div class="card__price">20,99 €</div>
      <div class="card__rule" style="top:189px"></div>
      <p class="card__text">Tiva Naturbalsam ist ein<br>natürliches Wohlfühlpro-<br>gramm für Muskeln,<br>Gelenke, Knochen, Nerven,<br>Sehnen und Bänder sowie<br>bei Prellungen und<br>Verbrennungen. Betroffene<br>können die entspannende</p>
    </article>

    <article class="card card--premium">
      <div class="card__seal"></div>
      <h2 class="card__label">PREMIUM</h2>
      <div class="card__qty">20 Tuben</div>
      <div class="card__rule" style="top:147px"></div>
      <div class="card__price">20,99 €</div>
      <div class="card__rule" style="top:189px"></div>
      <p class="card__text">Tiva Naturbalsam ist ein<br>natürliches Wohlfühlpro-<br>gramm für Muskeln,<br>Gelenke, Knochen, Nerven,<br>Sehnen und Bänder sowie<br>bei Prellungen und<br>Verbrennungen. Betroffene<br>können die entspannende</p>
    </article>

    <article class="card card--special">
      <div class="card__seal"></div>
      <h2 class="card__label">SPECIAL</h2>
      <div class="card__qty">50 Tuben</div>
      <div class="card__rule" style="top:147px"></div>
      <div class="card__price">20,99 €</div>
      <div class="card__rule" style="top:189px"></div>
      <p class="card__text">Tiva Naturbalsam ist ein<br>natürliches Wohlfühlpro-<br>gramm für Muskeln,<br>Gelenke, Knochen, Nerven,<br>Sehnen und Bänder sowie<br>bei Prellungen und<br>Verbrennungen. Betroffene<br>können die entspannende</p>
    </article>
  </section>

  <footer class="footer">
    <div class="footer__col" style="left:36px"><b>Lindauer Medizin Vertrieb GmbH</b><br>Birkenweg 14<br>80331 München<br>Deutschland</div>
    <div class="footer__sep" style="left:168px"></div>
    <div class="footer__col label-row" style="left:176px"><span>Telefon:</span>0049 89 123 456 70<br><span>Telefax:</span>0049 89 123 456 71<br><span>E-Mail:</span>bestellung@tiva-salbe.de<br><span>Internet:</span>www.tiva-salbe.de</div>
    <div class="footer__sep" style="left:347px"></div>
    <div class="footer__col" style="left:355px"><b>Gesellschafter:</b> Jonas Keller<br>Gesellschaft mit beschränkter Haftung<br>Amtsgericht München | HRB 100234<br>St.-Nr.: 111/222/33344</div>
    <div class="footer__sep" style="left:504px"></div>
    <div class="footer__col" style="left:512px">Isarbank<br><b>IBAN</b> DE00 1234 5678 9012 3456 78<br><b>BIC</b> &nbsp;ISARDEMMXXX</div>
    <div class="footer__rule"></div>
    <div class="footer__badges">
      <div class="badge" style="left:68px"></div>
      <div class="badge" style="left:151px"></div>
      <div class="badge" style="left:232px"></div>
      <div class="badge" style="left:317px"></div>
      <div class="badge" style="left:402px"></div>
      <div class="badge" style="left:485px"></div>
      <div class="badge badge--wide" style="left:571px"></div>
    </div>
  </footer>
</main>
</body>
</html>
```